Visitenkarte für therapeutischen Dienstleister
Breits die ersten Designvorschläge deckten sich weitgehend mit meinem Briefing. Anfragen und Änderungen werden rasch und professionell beantwortet und umgesetzt.
Zielgruppe
siehe Briefing
Aufgabenstellung

```html
<!DOCTYPE html>
<html lang="fr">
<head>
<meta charset="utf-8">
<title>Vitalis Soins – cartes de visite</title>
<link href="https://fonts.googleapis.com/css2?family=Russo+One&family=Montserrat:ital,wght@0,400;0,700;1,400&display=swap" rel="stylesheet">
<style>
  :root{
    --page:#fbfbfb;
    --slate:#3a464d;
    --red:#c8283a;
    --white:#ffffff;
  }
  *{margin:0;padding:0;box-sizing:border-box}
  html,body{width:672px;height:1200px;overflow:hidden;background:var(--page)}
  body{position:relative;font-family:"Montserrat",sans-serif}
  .card{position:absolute;background:var(--white);overflow:hidden}
  .card--dark{background:var(--slate)}
  .card--hero{left:176px;width:320px;height:214px}
  .card--half{width:270px;height:181px}
  .brand-mark{position:absolute;border-radius:50%;border:6px solid var(--red)}
  .brand-name{position:absolute;font-family:"Russo One",sans-serif;color:var(--slate);line-height:.95}
  .card--dark .brand-name{color:var(--white)}
  .card--hero .brand-mark{left:40px;top:46px;width:122px;height:122px}
  .card--hero .brand-name{left:160px;top:66px;font-size:44px}
  .card--half .brand-name{left:58px;top:42px;font-size:32px}
  .person{position:absolute;left:59px;top:112px;font-weight:700;font-size:13.5px;color:var(--slate)}
  .role{position:absolute;left:59px;top:127px;font-style:italic;font-size:8px;color:var(--slate)}
  .card--dark .person,.card--dark .role{color:var(--white)}
  .contact{position:absolute;left:106px;top:34px;list-style:none;font-size:8.4px;color:var(--slate);line-height:9.7px}
  .contact li{display:flex;align-items:flex-start;gap:3px}
  .contact .ico{width:8px;height:8px;flex:none;margin-top:.5px}
  .contact .indent{padding-left:11px}
  .services{position:absolute;left:73px;top:97px;list-style:none;font-style:italic;font-size:8.2px;color:var(--slate);line-height:9.7px}
  .card--dark .contact,.card--dark .services{color:var(--white)}
  .sep{color:var(--red);font-style:normal}
</style>
</head>
<body>

<section class="card card--hero" style="top:161px">
  <span class="brand-mark"></span>
  <div class="brand-name">Vitalis<br>Soins</div>
</section>

<section class="card card--half" style="left:62px;top:415px">
  <div class="brand-name">Vitalis<br>Soins</div>
  <div class="person">Luc Marbier</div>
  <div class="role">masseur médical avec brevet fédéral</div>
</section>

<section class="card card--half" style="left:340px;top:415px">
  <ul class="contact">
    <li><svg class="ico" viewBox="0 0 10 10"><circle cx="5" cy="5" r="5" fill="#c8283a"/><path d="M5 2.2a2 2 0 0 0-2 2c0 1.4 2 3.6 2 3.6s2-2.2 2-3.6a2 2 0 0 0-2-2z" fill="#fff"/></svg>Ch. des Tilleuls 14</li>
    <li class="indent">12XX Genève</li>
    <li><svg class="ico" viewBox="0 0 10 10"><circle cx="5" cy="5" r="5" fill="#c8283a"/><path d="M3.2 2.6l1 .9-.5.8c.4.8 1 1.4 1.8 1.8l.8-.5.9 1-.7.8C4.9 7 3 5.1 2.4 3.4z" fill="#fff"/></svg>T +41 XX XXX XX XX</li>
    <li><svg class="ico" viewBox="0 0 10 10"><circle cx="5" cy="5" r="5" fill="#c8283a"/><circle cx="5" cy="5" r="2.7" fill="none" stroke="#fff" stroke-width=".7"/><path d="M2.3 5h5.4M5 2.3v5.4" stroke="#fff" stroke-width=".6"/></svg>www.vitalis-soins.ch</li>
  </ul>
  <ul class="services">
    <li>Massage classique <span class="sep">|</span> Drainage lymphatique</li>
    <li>Électrothérapie <span class="sep">|</span> Hydrothérapie</li>
    <li>Tissu conjonctif <span class="sep">|</span> Réflexologie plantaire</li>
    <li>Cataplasmes <span class="sep">/</span> Enveloppements</li>
  </ul>
</section>

<section class="card card--half card--dark" style="left:62px;top:604px">
  <div class="brand-name">Vitalis<br>Soins</div>
  <div class="person">Luc Marbier</div>
  <div class="role">masseur médical avec brevet fédéral</div>
</section>

<section class="card card--half card--dark" style="left:340px;top:604px">
  <ul class="contact">
    <li><svg class="ico" viewBox="0 0 10 10"><circle cx="5" cy="5" r="5" fill="#c8283a"/><path d="M5 2.2a2 2 0 0 0-2 2c0 1.4 2 3.6 2 3.6s2-2.2 2-3.6a2 2 0 0 0-2-2z" fill="#3a464d"/></svg>Ch. des Tilleuls 14</li>
    <li class="indent">12XX Genève</li>
    <li><svg class="ico" viewBox="0 0 10 10"><circle cx="5" cy="5" r="5" fill="#c8283a"/><path d="M3.2 2.6l1 .9-.5.8c.4.8 1 1.4 1.8 1.8l.8-.5.9 1-.7.8C4.9 7 3 5.1 2.4 3.4z" fill="#3a464d"/></svg>T +41 XX XXX XX XX</li>
    <li><svg class="ico" viewBox="0 0 10 10"><circle cx="5" cy="5" r="5" fill="#c8283a"/><circle cx="5" cy="5" r="2.7" fill="none" stroke="#3a464d" stroke-width=".7"/><path d="M2.3 5h5.4M5 2.3v5.4" stroke="#3a464d" stroke-width=".6"/></svg>www.vitalis-soins.ch</li>
  </ul>
  <ul class="services">
    <li>Massage classique <span class="sep">|</span> Drainage lymphatique</li>
    <li>Électrothérapie <span class="sep">|</span> Hydrothérapie</li>
    <li>Tissu conjonctif <span class="sep">|</span> Réflexologie plantaire</li>
    <li>Cataplasmes <span class="sep">/</span> Enveloppements</li>
  </ul>
</section>

<section class="card card--hero card--dark" style="top:825px">
  <span class="brand-mark"></span>
  <div class="brand-name">Vitalis<br>Soins</div>
</section>

</body>
</html>
```